Cabling Business Graphic Design for Website

Hi,

We need a three pages designed for a cabling website: http://www.wirovant.com.au/

1.) Homepage
2.) Category Page
3.) Product Page

Wirovant is an online wholesaler of Server Racks and Cables.

Wirovant began in 2006 as an offshoot of a cabling installation company called Pyrosmel which has been around since 1993. Through Pyrosmel and the industry insight that gave use we saw the need for a direct, online wholesaler.

The problem we found the with the industry is the middle man. It seemed that industry suppliers were so obsessed with carving out distribution channels and establishing exclusive resellers and wholesalers that they began to alienate their products and price themselves out of the market.

Then came Wirovant - the first direct online data comms wholesaler to hit the industry.

We manufacture, import and sell direct - we have no middle men, keep our prices fair and our product range fresh.

Top three competitors:
Orbison Quarry - www.dulmep.com.au
Shelvantix - www.shelvantix.com.au
Brimtoll Messaging - www.brimtoll.net.au

Our range - we offer a massive range of products - we are always adding new and unique products.

Our Service - we have technical sales staff who are able to help with technical questions and provide advice on how to do things / what to buy - its not just a call centre situation.

We are able to custom manufacture cables and cabinets to suit specifications.

Its very easy to order from us, our turnaround time is 99% of the time 24 hours.

Please refer to the design brief file and the business uncovery for more information. The design brief files are quite specific so please ensure the design adheres to this brief.

Target Market(s)

IT Managers, Electricians, Network Integrators and IT companies.

They have a contract with schools and government departments to order their supplies. This is a massive section of their market.

Industry/Entity Type

Industry

Requirements
Must have
• Reinforce
* that the products adhere to government and industry certifications
* warranty / quality guarantee
* delivery details / stock availability
Nice to have
• Included in the Business Uncovery file
Should not have
• Included in the Business Uncovery

```html
<!DOCTYPE html>
<html lang="en">
<head>
<meta charset="utf-8">
<title>Wirovant – Home</title>
<link href="https://fonts.googleapis.com/css2?family=Arimo:wght@400;700&family=Tinos:ital,wght@0,400;0,700;1,400&display=swap" rel="stylesheet">
<style>
:root{
  --red:#c41a10;
  --red-dark:#8e120b;
  --ink:#111214;
  --ink-2:#1c1d22;
  --grey-bg:#f1f1f1;
  --line:#d8d8d8;
  --text:#555;
  --white:#fff;
}
*{box-sizing:border-box;margin:0;padding:0}
html,body{width:874px;height:1200px;overflow:hidden}
body{position:relative;background:var(--white);font-family:Arimo,Arial,sans-serif;color:var(--text);font-size:11px}
.abs{position:absolute}
.header{left:0;top:0;width:874px;height:126px;background:var(--ink);border-top:4px solid var(--red)}
.logo{left:56px;top:40px;display:flex;align-items:center;gap:8px;color:var(--white);font-weight:700;font-size:30px}
.logo i{width:14px;height:14px;background:var(--red);display:block}
.search{left:248px;top:50px;width:420px;height:50px;background:var(--red);padding:12px 10px;display:flex;gap:6px}
.search span{flex:1;background:var(--white);border-radius:3px;font-size:10px;color:#888;padding:7px 8px}
.search b{width:80px;background:var(--ink-2);color:var(--white);border-radius:3px;font-size:13px;font-weight:400;text-align:center;padding:6px 0}
.support{left:694px;top:40px;color:var(--white);font-size:10px;line-height:16px}
.support .agent{position:absolute;left:0;top:0;width:26px;height:30px;border-radius:4px;background:linear-gradient(#d35a3e,#7a2018)}
.support .txt{margin-left:48px}
.support .phone{position:absolute;left:14px;top:36px}
.support .num{position:absolute;left:48px;top:33px;font-size:15px;white-space:nowrap}
.support .hours{position:absolute;left:38px;top:68px;white-space:nowrap;font-size:9.5px}
.nav{left:0;top:126px;width:874px;height:30px;background:linear-gradient(var(--red),var(--red-dark));display:flex;align-items:center;padding-left:51px;gap:8px}
.nav a{color:var(--white);text-decoration:none;font-size:10px;white-space:nowrap}
.nav a.acc{color:var(--ink);margin-left:10px}
.side{left:40px;top:165px;width:159px;height:322px;border:1px solid var(--line);background:var(--grey-bg)}
.side li{list-style:none;height:24px;border-bottom:1px solid var(--line);background:var(--white);font-size:10.5px;font-weight:700;color:#333;padding:6px 8px;position:relative}
.side li.tall{height:48px}
.side li svg{position:absolute;right:7px;top:8px}
.main-h{left:212px;top:170px;font-size:16px;color:#444;font-weight:400}
.intro{left:212px;top:200px;width:455px;font-size:10.4px;line-height:16px}
.tile{background:var(--red);border:3px solid #ddd;box-shadow:0 0 0 1px #c8c8c8}
.lbl{font-size:11px;color:#555;text-align:center;letter-spacing:.5px}
.rule{left:208px;top:529px;width:460px;border-top:3px dotted #bbb}
.bar{left:208px;top:540px;width:460px;height:28px;background:linear-gradient(var(--red),var(--red-dark));color:var(--white);font-size:15px;padding:5px 7px}
.bar small{position:absolute;right:10px;top:8px;font-size:10px;font-weight:700}
.box{left:675px;width:160px;border:1px solid var(--line);background:var(--grey-bg)}
.box h3{background:linear-gradient(var(--red),var(--red-dark));color:var(--white);font-weight:400;font-size:14px;padding:6px 10px;line-height:19px;white-space:nowrap}
.box h3.small{font-size:13px}
.btn{display:inline-block;border-radius:3px;font-size:10px;padding:5px 11px}
.footer-links{left:0;top:990px;width:874px;height:32px;background:var(--ink-2);color:#ddd;font-size:10px;display:flex;justify-content:center;align-items:center;gap:10px}
.footer{left:0;top:1022px;width:874px;height:146px;background:var(--ink)}
.col{top:1034px;color:#ddd;font-size:9.5px;line-height:16px;height:124px;padding-right:6px;border-right:1px solid #333;white-space:nowrap}
.col b{display:block;margin-bottom:6px;font-weight:400;font-size:9px}
.copy{left:0;top:1168px;width:874px;height:32px;background:#0b0b0c;color:#ccc;font-size:10px;text-align:center;padding-top:11px}
</style>
</head>
<body>
<header class="abs header"></header>
<div class="abs logo"><i></i>Wirovant</div>
<div class="abs search"><span>Search Term</span><b>Search</b></div>
<div class="abs support">
  <div class="agent" role="img" aria-label="Support agent illustration"></div>
  <div class="txt">Need Support?<br>Live Chat</div>
  <svg class="phone" width="12" height="14" viewBox="0 0 12 14"><path d="M2 1l3 0 1 3-2 2q1 3 4 4l2-2 3 1-1 3q-8 0-10-11z" fill="#fff"/></svg>
  <div class="num">1300 555 018</div>
  <div class="hours">Mon - Fri ( 9am - 5pm ) AEST</div>
</div>
<nav class="abs nav">
  <a>HOME</a><a>ABOUT US</a><a>OUR CATALOGUE</a><a>WHOLESALE OUTLET STORES</a><a>EDUCATION / GOVERNMENT</a><a>SHIPPING</a><a>PAYMENTS</a><a>CONTACT US</a><a class="acc">ACCOUNT / LOGIN</a>
</nav>

<ul class="abs side">
  <li>Cables<svg width="6" height="9"><path d="M1 1l4 3.5-4 3.5" stroke="#1b3a8a" stroke-width="2" fill="none"/></svg></li>
  <li>Data Product<svg width="6" height="9"><path d="M1 1l4 3.5-4 3.5" stroke="#1b3a8a" stroke-width="2" fill="none"/></svg></li>
  <li>Server Cabinets<svg width="6" height="9"><path d="M1 1l4 3.5-4 3.5" stroke="#1b3a8a" stroke-width="2" fill="none"/></svg></li>
  <li>Network Cabinets<svg width="6" height="9"><path d="M1 1l4 3.5-4 3.5" stroke="#1b3a8a" stroke-width="2" fill="none"/></svg></li>
  <li>Fiber Products<svg width="6" height="9"><path d="M1 1l4 3.5-4 3.5" stroke="#1b3a8a" stroke-width="2" fill="none"/></svg></li>
  <li>Coax Products<svg width="6" height="9"><path d="M1 1l4 3.5-4 3.5" stroke="#1b3a8a" stroke-width="2" fill="none"/></svg></li>
  <li>Telephone &amp; Voice<svg width="6" height="9"><path d="M1 1l4 3.5-4 3.5" stroke="#1b3a8a" stroke-width="2" fill="none"/></svg></li>
  <li class="tall">Tools &amp; Switches<br><br>&amp; Hardware<svg width="6" height="9"><path d="M1 1l4 3.5-4 3.5" stroke="#1b3a8a" stroke-width="2" fill="none"/></svg></li>
  <li>AV Wall Plates &amp; Inserts<svg width="6" height="9"><path d="M1 1l4 3.5-4 3.5" stroke="#1b3a8a" stroke-width="2" fill="none"/></svg></li>
  <li>Plasma &amp; LCD Brackets<svg width="6" height="9"><path d="M1 1l4 3.5-4 3.5" stroke="#1b3a8a" stroke-width="2" fill="none"/></svg></li>
  <li>Cable Ducting Conduit<svg width="6" height="9"><path d="M1 1l4 3.5-4 3.5" stroke="#1b3a8a" stroke-width="2" fill="none"/></svg></li>
</ul>

<h1 class="abs main-h">Lorem ipsum dolor sit amet, consectetuer</h1>
<p class="abs intro">Lorem ipsum dolor sit amet, consectetuer adipiscing elit. Aenean commodo ligula eget dolor. Aenean massa. Cum sociis natoque penatibus et magnis dis parturient montes, nascetur ridiculus mus. Donec quam felis, ultricies nec, pellentesque eu, pretium quis, sem. Nulla consequat massa quis enim. Donec pede justo, fringilla vel, aliquet nec, vulputate eget, arcu. In enim justo, rhoncus ut, imperdiet a, venenatis vitaLorem ipsum dolor sit amet, consectetuer adipiscing elit. Aenean commodo ligula eget dolor. Aenean massa. Cum sociis natoque penatibus et magnis dis parturient montes, nascetur ridiculus mus. Donec quam felis, ultricies nec, Aenean massa. Cum sociis natoque penatibus et magnis dis parturient montes, nascetur ridiculus mus.</p>

<div class="abs tile" style="left:209px;top:340px;width:104px;height:128px" role="img" aria-label="Cables category image"></div>
<div class="abs tile" style="left:327px;top:340px;width:104px;height:128px" role="img" aria-label="Cable management category image"></div>
<div class="abs tile" style="left:445px;top:340px;width:104px;height:128px" role="img" aria-label="Data products category image"></div>
<div class="abs tile" style="left:563px;top:340px;width:104px;height:128px" role="img" aria-label="Server rack cabinets category image"></div>
<div class="abs lbl" style="left:209px;top:476px;width:104px">Cables</div>
<div class="abs lbl" style="left:322px;top:476px;width:114px">Cable Management</div>
<div class="abs lbl" style="left:445px;top:476px;width:104px">Data Products</div>
<div class="abs lbl" style="left:563px;top:476px;width:104px">Server Rack<br>Cabinets</div>

<div class="abs rule"></div>
<div class="abs bar">Top Selling Products<small>more</small></div>

<div class="abs tile" style="left:209px;top:587px;width:102px;height:128px" role="img" aria-label="Network cable product image"></div>
<div class="abs tile" style="left:328px;top:587px;width:102px;height:128px" role="img" aria-label="Network cable product image"></div>
<div class="abs tile" style="left:447px;top:587px;width:102px;height:128px" role="img" aria-label="Network cable product image"></div>
<div class="abs tile" style="left:565px;top:587px;width:102px;height:128px" role="img" aria-label="Network cable product image"></div>
<div class="abs lbl" style="left:209px;top:726px;width:102px">Network Cable</div>
<div class="abs lbl" style="left:328px;top:726px;width:102px">Network Cable</div>
<div class="abs lbl" style="left:447px;top:726px;width:102px">Network Cable</div>
<div class="abs lbl" style="left:565px;top:726px;width:102px">Network Cable</div>

<div class="abs tile" style="left:209px;top:762px;width:102px;height:128px" role="img" aria-label="Network cable product image"></div>
<div class="abs tile" style="left:328px;top:762px;width:102px;height:128px" role="img" aria-label="Network cable product image"></div>
<div class="abs tile" style="left:447px;top:762px;width:102px;height:128px" role="img" aria-label="Network cable product image"></div>
<div class="abs tile" style="left:565px;top:762px;width:102px;height:128px" role="img" aria-label="Network cable product image"></div>
<div class="abs lbl" style="left:209px;top:906px;width:102px">Network Cable</div>
<div class="abs lbl" style="left:328px;top:906px;width:102px">Network Cable</div>
<div class="abs lbl" style="left:447px;top:906px;width:102px">Network Cable</div>
<div class="abs lbl" style="left:565px;top:906px;width:102px">Network Cable</div>

<section class="abs box" style="top:165px;height:162px">
  <h3>SHOPPING CART</h3>
  <div class="abs" style="left:16px;top:50px;width:42px;height:36px;border-radius:4px;background:linear-gradient(#f3c73a,#c98a10)" role="img" aria-label="Shopping basket illustration"></div>
  <div class="abs" style="left:72px;top:54px;font-size:10px;line-height:20px;color:#555">Items: 0<br>Total: $0.00</div>
  <span class="abs btn" style="left:14px;top:120px;background:var(--red);color:#fff">View cart</span>
  <span class="abs btn" style="left:82px;top:120px;background:#ddd;color:var(--red)">Checkout</span>
</section>
<section class="abs box" style="top:331px;height:42px;border:0">
  <h3 style="height:42px;padding-top:12px">WHY CLIENT?</h3>
  <div class="abs" style="left:118px;top:0;width:36px;height:42px;background:linear-gradient(#5b6b80,#2a2f3a)" role="img" aria-label="Businessman illustration"></div>
</section>
<section class="abs box" style="top:382px;height:168px">
  <h3 class="small">CERTIFICATES &amp;<br>QUALITY ASSURANCE</h3>
  <div class="abs" style="left:34px;top:64px;width:90px;height:74px;background:#fff;border:1px solid #ccc" role="img" aria-label="Certification badge"></div>
</section>
<section class="abs box" style="top:565px;height:160px">
  <h3>OUR NEWSLETTER</h3>
  <div class="abs" style="left:10px;top:36px;font-size:11px;font-weight:700;color:#555;white-space:nowrap">JOIN OUR NEWSLETTER</div>
  <div class="abs" style="left:10px;top:53px;width:140px;font-size:10px;line-height:14px;color:#777">Discover exclusive offers, products previews and much more......</div>
  <div class="abs" style="left:8px;top:101px;width:142px;height:20px;background:#fff;border:1px solid #bbb;font-size:9.5px;color:#888;padding:4px 6px">Enter your mail</div>
  <div class="abs" style="left:8px;top:132px;width:138px;height:24px;border-radius:4px;background:var(--ink-2);color:#fff;font-size:11px;font-weight:700;text-align:center;padding-top:6px">GET SPECIAL OFFERS</div>
</section>
<section class="abs box" style="top:745px;height:70px">
  <div class="abs" style="left:12px;top:12px;display:flex;gap:5px">
    <i style="width:28px;height:16px;background:#fff;border:1px solid #bbb" role="img" aria-label="Payment card"></i>
    <i style="width:28px;height:16px;background:#fff;border:1px solid #bbb" role="img" aria-label="Payment card"></i>
    <i style="width:28px;height:16px;background:#fff;border:1px solid #bbb" role="img" aria-label="Payment card"></i>
    <i style="width:28px;height:16px;background:#fff;border:1px solid #bbb" role="img" aria-label="Payment service"></i>
  </div>
  <svg class="abs" style="left:16px;top:40px" width="12" height="15" viewBox="0 0 12 15"><path d="M3 7V4a3 3 0 016 0v3" stroke="#c41a10" stroke-width="2" fill="none"/><rect x="1" y="7" width="10" height="8" rx="1" fill="#c41a10"/></svg>
  <div class="abs" style="left:36px;top:41px;font-family:Tinos,serif;font-weight:700;font-size:11px;color:var(--red);white-space:nowrap">100% Secure shopping</div>
</section>
<section class="abs box" style="top:822px;height:153px">
  <h3>TESTIMONIALS</h3>
  <div class="abs" style="left:8px;top:38px;width:144px;height:82px;background:#e2e2e2"></div>
  <div class="abs" style="left:10px;top:28px;font-family:Tinos,serif;font-size:46px;color:#c8c8c8">“</div>
  <div class="abs" style="left:18px;top:42px;width:130px;font-family:Tinos,serif;font-style:italic;font-size:10.5px;line-height:14px;color:#555;text-align:right">Lorem ipsum dolor sitmet, consectetuer adipi-scing elit. Aenean commodo ligula eget dolor. Aenean massa. Cum sociis nat.</div>
  <div class="abs" style="left:18px;top:126px;font-size:10px;color:#444">NAME</div>
  <div class="abs" style="left:102px;top:140px;font-size:10px;color:var(--red)">View more</div>
</section>

<div class="abs footer-links">
  <span>Home</span>|<span>About Wirovant</span>|<span>My Account</span>|<span>Order Status</span>|<span>Wish List</span>|<span>Gift Certificate</span>|<span>View Cart</span>|<span>Sign In</span>|<span>Create An Account</span>
</div>
<div class="abs footer"></div>
<div class="abs col" style="left:40px;width:236px"><b>SERVER RACKS / NETWORK COMPUTER CABINETS</b>Network Cabinet &amp; Rack Mount Accesories<br>Wall Mount Network Cabinets<br>Half Height Floor Server Racks<br>Full Height Server Racks<br>Wall Mount Frames<br>Network Cabinet Shelves</div>
<div class="abs col" style="left:285px;width:132px"><b>CABLE MANAGEMENT</b>Cable Management Rings<br>Cable Floor Covers<br>Cable Management Rails<br>Cable Ties<br>Cable Tray</div>
<div class="abs col" style="left:430px;width:100px"><b>ETHERNET CABLES</b>Cat 5E Cable<br>Cat 6 Cable</div>
<div class="abs col" style="left:542px;width:172px"><b>FIBRE PRODUCTS</b>Multimode Fibre Optic Patch Cables<br>Single Mode Fibre Optic Patch Leads<br>Fibre Optic Cable</div>
<div class="abs col" style="left:724px;width:110px;border:0"><b>PATCH PANELS</b>Cat5e Patch Panel<br>Cat 6 Patch Panels</div>
<div class="abs copy">Copyright 2011 Wirovant. All rights reserved. Terms and conditions</div>
<div class="abs" style="left:750px;top:1175px;width:18px;height:18px;background:#3b5a9a" role="img" aria-label="Social link"></div>
<div class="abs" style="left:778px;top:1175px;width:18px;height:18px;background:#3ba6d8" role="img" aria-label="Social link"></div>
</body>
</html>
```